new roofing company card

New primary business card for roofing company.

Industry/Entity Type

Residential roofing/Specializing in Asphalt and Standing seam metal roofing

Contact Information for Business Card

Phone number is: 484 672 1058 Email: support@fennridgeroofworks.com website: www.fennridgeroofworks.com

Colors
EB3D1F
EC4F4E
F09395
F8D3D4
FCEDEE

```html
<!DOCTYPE html>
<html lang="en">
<head>
<meta charset="utf-8">
<title>Fennridge Roofworks — Business Card</title>
<link rel="stylesheet" href="https://fonts.googleapis.com/css2?family=Cinzel:wght@500;600&family=Crimson+Text:wght@400&display=swap">
<style>
  :root {
    --backdrop: #5a5a5c;
    --brand-red: #c3322a;
    --card-white: #ffffff;
    --ink: #222222;
    --rule: #3a3a3a;
    --dot-tint: #f8d3d4;
  }
  * { box-sizing: border-box; margin: 0; padding: 0; }
  html, body { width: 1200px; height: 1095px; overflow: hidden; }
  body {
    background: var(--backdrop);
    position: relative;
    font-family: "Crimson Text", serif;
  }
  .card {
    position: absolute;
    left: 220px;
    width: 760px;
    height: 434px;
    border-radius: 22px;
    box-shadow: 0 18px 40px rgba(0,0,0,0.35);
  }
  .card--front {
    top: 90px;
    background: var(--brand-red);
    display: flex;
    align-items: center;
    justify-content: center;
  }
  .card--back {
    top: 570px;
    background: var(--card-white);
  }
  .wordmark {
    font-family: "Cinzel", serif;
    font-weight: 600;
    text-align: center;
    line-height: 1.05;
    letter-spacing: 2px;
  }
  .wordmark__main { display: block; font-size: 64px; }
  .wordmark__sub { display: block; font-size: 30px; letter-spacing: 4px; margin-top: 6px; }
  .card--front .wordmark { color: var(--card-white); }
  .card--back .wordmark {
    position: absolute;
    left: 60px;
    top: 165px;
    width: 290px;
    color: var(--ink);
  }
  .card--back .wordmark__main { font-size: 42px; }
  .card--back .wordmark__sub { font-size: 20px; }
  .divider {
    position: absolute;
    left: 385px;
    top: 130px;
    width: 1.5px;
    height: 175px;
    background: var(--rule);
  }
  .dot-field {
    position: absolute;
    right: 70px;
    top: 40px;
    width: 170px;
    height: 100px;
    background: var(--dot-tint);
    opacity: 0.6;
    border-radius: 4px;
  }
  .contact {
    position: absolute;
    left: 420px;
    top: 138px;
  }
  .contact__name {
    font-family: "Cinzel", serif;
    font-weight: 500;
    font-size: 30px;
    color: var(--ink);
    letter-spacing: 1px;
  }
  .contact__name .first { color: var(--brand-red); }
  .contact__role {
    font-size: 16px;
    color: var(--ink);
    margin-top: 2px;
  }
  .contact__accent {
    width: 68px;
    height: 3px;
    background: var(--brand-red);
    margin: 8px 0 14px;
  }
  .contact__list { list-style: none; }
  .contact__item {
    display: flex;
    align-items: center;
    gap: 10px;
    font-size: 17px;
    color: var(--ink);
    margin-bottom: 8px;
    letter-spacing: 0.3px;
  }
  .contact__item svg { width: 15px; height: 15px; flex: none; }
</style>
</head>
<body>
  <section class="card card--front">
    <div class="wordmark">
      <span class="wordmark__main">FENNRIDGE</span>
      <span class="wordmark__sub">ROOFWORKS</span>
    </div>
  </section>

  <section class="card card--back">
    <div class="dot-field" role="img" aria-label="Decorative grid of small red dots"></div>
    <div class="wordmark">
      <span class="wordmark__main">FENNRIDGE</span>
      <span class="wordmark__sub">ROOFWORKS</span>
    </div>
    <div class="divider"></div>
    <div class="contact">
      <h1 class="contact__name"><span class="first">DALE</span> MORROW</h1>
      <p class="contact__role">Owner</p>
      <div class="contact__accent"></div>
      <ul class="contact__list">
        <li class="contact__item">
          <svg viewBox="0 0 16 16" aria-hidden="true"><path fill="#c3322a" d="M3.5 1.5l2.5 0 1 3.5-1.7 1.2a8 8 0 0 0 4.5 4.5l1.2-1.7 3.5 1v2.5c0 .8-.7 1.5-1.5 1.5A12.5 12.5 0 0 1 2 3c0-.8.7-1.5 1.5-1.5z"/></svg>
          <span>484 672 1058</span>
        </li>
        <li class="contact__item">
          <svg viewBox="0 0 16 16" aria-hidden="true"><rect x="1" y="3" width="14" height="10" rx="1" fill="#c3322a"/><path d="M1.5 3.8L8 9l6.5-5.2" stroke="#fff" stroke-width="1.3" fill="none"/></svg>
          <span>support@fennridgeroofworks.com</span>
        </li>
        <li class="contact__item">
          <svg viewBox="0 0 16 16" aria-hidden="true"><circle cx="8" cy="8" r="7" fill="#c3322a"/><path d="M1 8h14M8 1c-3 3.5-3 10.5 0 14M8 1c3 3.5 3 10.5 0 14" stroke="#fff" stroke-width="1" fill="none"/></svg>
          <span>www.fennridgeroofworks.com</span>
        </li>
      </ul>
    </div>
  </section>
</body>
</html>
```